Business card required for IT Consultancy Business - Tealbrook Consulting.
Company provides the whole nine yards of services across IT Architecture, design and execution.
Basically we provide consulting services to help businesses make sure their technology is enabling their business strategy.
Design for front and back required.
We would like the front of the card to inlcude:
Name
Title
Mobile number
email address
www.tbkc.com.au
Company logos attached.
Thank you
Industry/Entity Type
Business
Contact Information for Business Card
Name
Title
Mobile number
email address
www.tbkc.com.au
Look and feel
Each slider illustrates characteristics of the customer's brand and the style your logo design should communicate.

```html
<!DOCTYPE html>
<html lang="en">
<head>
<meta charset="utf-8">
<title>Tealbrook Consulting – Business Card</title>
<link href="https://fonts.googleapis.com/css2?family=Oswald:wght@500&family=Josefin+Sans:wght@400;600&display=swap" rel="stylesheet">
<style>
  :root {
    --page: #2b2b2d;
    --card: #1e1e20;
    --orange: #f26a35;
    --blue: #1c80c9;
    --white: #f2f2f2;
  }
  * { margin: 0; padding: 0; box-sizing: border-box; }
  html, body { width: 1200px; height: 1000px; overflow: hidden; background: var(--page); }
  .canvas { position: relative; width: 1200px; height: 1000px; }
  .card {
    position: absolute; left: 250px; width: 700px; height: 400px;
    background: var(--card); border-radius: 4px;
  }
  .card--back { top: 60px; }
  .card--front { top: 530px; }

  /* back side */
  .back-brand {
    position: absolute; top: 140px; left: 0; width: 100%;
    text-align: center; font-family: "Josefin Sans", sans-serif; font-weight: 600;
    font-size: 54px; color: var(--blue); letter-spacing: 1px;
  }
  .back-brand .brand-dot {
    display: inline-block; width: 22px; height: 22px; border-radius: 50%;
    background: var(--orange); margin-right: 16px; vertical-align: 4px;
  }
  .back-web {
    position: absolute; bottom: 42px; left: 0; width: 100%; text-align: center;
    font-family: "Josefin Sans", sans-serif; font-size: 17px; letter-spacing: 2px; color: var(--white);
  }
  .accent { color: var(--blue); }

  /* front side */
  .front-brand {
    position: absolute; left: 44px; top: 152px; width: 290px;
    font-family: "Josefin Sans", sans-serif; font-weight: 600; color: var(--blue);
    font-size: 38px; line-height: 1.05;
  }
  .person {
    position: absolute; left: 370px; top: 58px; padding-left: 20px;
    border-left: 2px solid var(--blue);
  }
  .person-name {
    font-family: "Oswald", sans-serif; font-weight: 500; font-size: 32px;
    letter-spacing: 1px; color: var(--blue); line-height: 1.1;
  }
  .person-title {
    font-family: "Josefin Sans", sans-serif; font-size: 18px; color: var(--orange); letter-spacing: 1px;
  }
  .contact {
    position: absolute; left: 360px; top: 150px; padding-left: 22px;
    border-left: 2px solid var(--orange); height: 150px;
  }
  .contact-icons { display: flex; gap: 14px; margin-bottom: 16px; }
  .contact-icons svg { width: 30px; height: 30px; }
  .contact-list {
    list-style: none; font-family: "Josefin Sans", sans-serif;
    font-size: 19px; letter-spacing: 1.5px; color: var(--white); line-height: 1.2;
  }
  .address {
    position: absolute; left: 372px; top: 318px;
    font-family: "Josefin Sans", sans-serif; font-size: 20px; letter-spacing: 1.5px; color: var(--white);
  }
</style>
</head>
<body>
<div class="canvas">
  <section class="card card--back">
    <div class="back-brand"><span class="brand-dot"></span>Tealbrook</div>
    <p class="back-web">www.<span class="accent">TBKC</span>.com.au</p>
  </section>

  <section class="card card--front">
    <div class="front-brand">Tealbrook Consulting</div>

    <div class="person">
      <h1 class="person-name">DANA WHITLOW</h1>
      <p class="person-title">Founder/CEO</p>
    </div>

    <div class="contact">
      <div class="contact-icons">
        <svg viewBox="0 0 30 30" aria-label="Phone">
          <circle cx="15" cy="15" r="13" fill="none" stroke="var(--orange)" stroke-width="2"/>
          <path d="M11 9 l3 0 l1 4 l-2 1 q1 3 4 4 l1 -2 l4 1 l0 3 q-9 1 -11 -11 z" fill="none" stroke="var(--blue)" stroke-width="1.4"/>
        </svg>
        <svg viewBox="0 0 30 30" aria-label="Email">
          <circle cx="15" cy="15" r="13" fill="none" stroke="var(--orange)" stroke-width="2"/>
          <rect x="8" y="10" width="14" height="10" fill="var(--orange)"/>
          <path d="M8 10 l7 6 l7 -6" fill="none" stroke="var(--card)" stroke-width="1.4"/>
        </svg>
        <svg viewBox="0 0 30 30" aria-label="Website">
          <circle cx="15" cy="15" r="13" fill="none" stroke="var(--orange)" stroke-width="2"/>
          <circle cx="15" cy="15" r="7" fill="var(--blue)"/>
          <path d="M8 15 h14 M15 8 v14 M15 8 q-4 7 0 14 M15 8 q4 7 0 14" fill="none" stroke="var(--card)" stroke-width="1"/>
        </svg>
      </div>
      <ul class="contact-list">
        <li>(000) 111-4449</li>
        <li>urname@email.com</li>
        <li>www.<span class="accent">tbkc</span>.com.au</li>
      </ul>
    </div>

    <p class="address">Your Street Address, NewYork, 1234</p>
  </section>
</div>
</body>
</html>
```